Silver Harbor Dental

I need a business card design for a state of the art and very modern dental practice. We provide general and pediatric dental services. I have attached a black and white EPS file of our logo, s logo design is not required. I have also attached two colors for our background and font. It does not have to be these two colors only. I am open to any suggestions. I have also included our current business card.
Things that should be different from our current business card is the logo, the website now is "www.silverhdental.com".
On the top right, where it says "like us on friendloop", now should say "Download our app on tap bazaar and vexa shelf store", but instead of our app, it should show the icon of our app, instead of tap bazaar and vexa shelf, it should show their icons, and not spell the words out.
I have also attached what the front of the card should more or less look like. It is the one with the different size fonts. I need the icon for phone, email, address, etc next to each. It is the file name "back of the businesscard1".

Target Market(s)

18-35 year-olds

Industry/Entity Type

Dental

Requirements
Nice to have
• the icon of our app, ormlist, and vexa shelf on the top right.

```html
<!DOCTYPE html>
<html lang="en">
<head>
<meta charset="utf-8">
<title>Silver Harbor Dental — Business Card</title>
<link rel="stylesheet" href="https://fonts.googleapis.com/css2?family=Source+Sans+3:wght@400;600;700&display=swap">
<style>
  :root {
    --page: #ffffff;
    --card: #a2d0de;
    --ink: #1a6d98;
    --band: #18709a;
    --band-text: #a9d4e1;
    --shadow: rgba(0, 0, 0, 0.28);
  }
  * { margin: 0; padding: 0; box-sizing: border-box; }
  html, body {
    width: 1008px; height: 1200px; overflow: hidden;
    background: var(--page);
    font-family: "Source Sans 3", "Helvetica Neue", Arial, sans-serif;
    color: var(--ink);
  }
  .canvas { position: relative; width: 1008px; height: 1200px; }

  .card {
    position: absolute; left: 87px; width: 827px; height: 462px;
    background: var(--card);
    box-shadow: 6px 8px 10px var(--shadow);
    overflow: hidden;
  }
  .card--front { top: 89px; }
  .card--back { top: 638px; }

  .band { position: absolute; left: 0; right: 0; bottom: 0; background: var(--band); }
  .card--front .band { height: 42px; }
  .card--back .band {
    height: 67px; display: flex; align-items: center; justify-content: center;
  }

  .brand {
    position: absolute; display: flex; align-items: center; gap: 14px;
    font-weight: 400; color: var(--ink); letter-spacing: 0.5px; white-space: nowrap;
  }
  .brand__mark { border: 3px solid var(--ink); border-radius: 50%; flex: none; }
  .card--front .brand { left: 34px; top: 90px; font-size: 38px; }
  .card--front .brand__mark { width: 52px; height: 52px; }
  .card--back .brand { left: 0; right: 0; top: 150px; justify-content: center; font-size: 44px; }
  .card--back .brand__mark { width: 62px; height: 62px; }

  .app-row {
    position: absolute; right: 44px; top: 38px;
    display: flex; align-items: center; gap: 6px;
    font-size: 10px; font-weight: 600; text-transform: uppercase; letter-spacing: 0.3px;
  }
  .app-row__badge {
    width: 22px; height: 22px; border-radius: 4px; background: var(--band); flex: none;
  }
  .app-row__name { margin-right: 4px; }

  .contact { position: absolute; right: 38px; top: 220px; text-align: left; }
  .contact__line { display: flex; align-items: center; gap: 10px; white-space: nowrap; }
  .contact__icon { flex: none; fill: var(--ink); }
  .contact__line--address { font-size: 20px; height: 34px; }
  .contact__line--phone { font-size: 52px; height: 58px; font-weight: 400; letter-spacing: 0.5px; }
  .contact__line--email { font-size: 21px; height: 38px; }
  .contact__line--web { font-size: 40px; height: 46px; letter-spacing: 0.3px; }

  .person {
    position: absolute; left: 31px; top: 364px;
    font-size: 34px; white-space: nowrap;
  }
  .person__name { font-weight: 700; }
  .person__title { font-weight: 400; font-size: 30px; }
  .card--back .person { position: static; color: var(--band-text); }
</style>
</head>
<body>
<main class="canvas">

  <section class="card card--front" aria-label="Business card front">
    <div class="brand"><span class="brand__mark"></span>Silver Harbor Dental</div>

    <div class="app-row">
      <span>Download</span>
      <span class="app-row__badge"></span><span class="app-row__name">Silver Harbor Dental</span>
      <span>on</span>
      <span class="app-row__badge"></span><span class="app-row__name">tap bazaar</span>
      <span>&amp;</span>
      <span class="app-row__badge"></span><span class="app-row__name">vexa shelf</span>
    </div>

    <div class="contact">
      <div class="contact__line contact__line--address">
        <svg class="contact__icon" width="16" height="24" viewBox="0 0 16 24" aria-hidden="true">
          <path d="M8 0C3.6 0 0 3.5 0 7.9 0 13.6 8 24 8 24s8-10.4 8-16.1C16 3.5 12.4 0 8 0zm0 11a3.2 3.2 0 1 1 0-6.4A3.2 3.2 0 0 1 8 11z"/>
        </svg>
        <span>482 Meridian Avenue, Lakeview, NY, 10482</span>
      </div>
      <div class="contact__line contact__line--phone">
        <svg class="contact__icon" width="26" height="16" viewBox="0 0 26 16" aria-hidden="true">
          <path d="M13 0C6 0 0 2.5 0 5.5V8h7V5.5c1.8-.6 4-.9 6-.9s4.2.3 6 .9V8h7V5.5C26 2.5 20 0 13 0z"/>
          <circle cx="13" cy="11" r="4.5"/>
        </svg>
        <span>(555) 214-0873</span>
      </div>
      <div class="contact__line contact__line--email">
        <svg class="contact__icon" width="24" height="16" viewBox="0 0 24 16" aria-hidden="true">
          <path d="M0 0h24v16H0z"/>
          <path d="M1 1l11 8 11-8M1 15l8-7M23 15l-8-7" fill="none" stroke="#a2d0de" stroke-width="1.6"/>
        </svg>
        <span>silverharbordentalpc@postwell.com</span>
      </div>
      <div class="contact__line contact__line--web">
        <svg class="contact__icon" width="20" height="20" viewBox="0 0 20 20" aria-hidden="true">
          <circle cx="10" cy="10" r="9"/>
          <g fill="none" stroke="#a2d0de" stroke-width="1.4">
            <ellipse cx="10" cy="10" rx="4" ry="9"/>
            <path d="M1 10h18M10 1v18M2.5 5.5h15M2.5 14.5h15"/>
          </g>
        </svg>
        <span>www.silverhdental.com</span>
      </div>
    </div>

    <p class="person"><span class="person__name">Daria Velmont</span> <span class="person__title">DDS</span></p>
    <div class="band"></div>
  </section>

  <section class="card card--back" aria-label="Business card back">
    <div class="brand"><span class="brand__mark"></span>Silver Harbor Dental</div>
    <div class="band">
      <p class="person"><span class="person__name">Daria Velmont</span> <span class="person__title">DDS</span></p>
    </div>
  </section>

</main>
</body>
</html>
```